KVT Business Cards

We require business cards for our business. We would like a matte black back to the card, with our logo centred in the middle. The front side of the card is open to design.

Target Market(s)

Clients looking for legal services (professional)

Industry/Entity Type

Legal

Contact Information for Business Card

Boris Telemark
Partner
Mobile: 0438 715 642
Email: boris@kvtlaw.co
Website: www.kvtlaw.co
Level 3, 118 Wexbury Street
Sydney NSW 2000

Font styles to use
Other font styles liked:
• Avenir

Colors
f04a50
ffffff
1b1b1b

Requirements
Must have
• Black back with logo included in the centre of the card.
• Our font is Avenir.

```html
<!DOCTYPE html>
<html lang="en">
<head>
<meta charset="utf-8">
<title>KVT Legal Business Cards</title>
<link rel="stylesheet" href="https://fonts.googleapis.com/css2?family=Montserrat:wght@400;500;600;700&display=swap">
<style>
  :root {
    --bg: #1c1c1c;
    --card-front: #ebebeb;
    --card-back: #0f0f0f;
    --ink: #1b1b1b;
    --accent: #c4173f;
    --emboss: #222222;
    --font: "Montserrat", sans-serif;
  }
  * { box-sizing: border-box; margin: 0; padding: 0; }
  html, body {
    width: 1200px; height: 1200px; overflow: hidden;
    background: var(--bg);
    font-family: var(--font);
  }
  .card {
    position: absolute;
    left: 227px;
    width: 746px;
    height: 425px;
  }
  .card--front { top: 135px; background: var(--card-front); color: var(--ink); }
  .card--back { top: 640px; background: var(--card-back); }

  .brand {
    position: absolute;
    display: flex; align-items: center; gap: 18px;
  }
  .brand__square { width: 34px; height: 34px; background: var(--accent); }
  .brand__name {
    font-weight: 700; font-size: 44px; letter-spacing: 0.5px; line-height: 1;
  }
  .card--front .brand { left: 36px; top: 110px; }
  .card--front .brand__name { color: var(--ink); }
  .card--back .brand { left: 50%; top: 50%; transform: translate(-50%, -50%); }
  .card--back .brand__square { background: var(--emboss); }
  .card--back .brand__name { color: var(--emboss); }

  .person { position: absolute; left: 36px; top: 238px; }
  .person__name { color: var(--accent); font-weight: 600; font-size: 22px; letter-spacing: 0.6px; }
  .person__role { font-size: 16px; margin-top: 4px; letter-spacing: 0.3px; }

  .divider { position: absolute; left: 0; right: 0; top: 302px; height: 2px; }
  .divider__line { position: absolute; top: 0; height: 1.5px; background: var(--ink); }
  .divider__line--left { left: 0; width: 35px; }
  .divider__line--right { left: 212px; right: 0; }
  .divider__dots {
    position: absolute; left: 37px; width: 173px; top: 0; height: 1.5px;
    background-image: radial-gradient(circle, var(--accent) 0.7px, transparent 0.8px);
    background-size: 3px 2px;
  }

  .contacts { position: absolute; left: 35px; top: 323px; list-style: none; }
  .contacts__item {
    display: flex; align-items: center; gap: 8px;
    font-size: 17px; height: 24px; letter-spacing: 0.3px;
  }
  .contacts__icon { width: 18px; height: 18px; flex: none; }
  .contacts__hl { color: var(--accent); }

  .address {
    position: absolute; right: 35px; top: 347px;
    text-align: right; font-size: 17px; line-height: 24px; letter-spacing: 0.3px;
    font-style: normal;
  }
</style>
</head>
<body>
  <section class="card card--front">
    <div class="brand">
      <span class="brand__square"></span>
      <span class="brand__name">KVT LEGAL</span>
    </div>

    <div class="person">
      <p class="person__name">Boris Telemark</p>
      <p class="person__role">Partner</p>
    </div>

    <div class="divider">
      <span class="divider__line divider__line--left"></span>
      <span class="divider__dots"></span>
      <span class="divider__line divider__line--right"></span>
    </div>

    <ul class="contacts">
      <li class="contacts__item">
        <svg class="contacts__icon" viewBox="0 0 18 18" aria-hidden="true">
          <circle cx="9" cy="9" r="9" fill="#c4173f"/>
          <path d="M4.5 7.5c0-1.5 2-2.3 4.5-2.3s4.5.8 4.5 2.3l-1.7.3-.3-1.1H6.5l-.3 1.1z" fill="#fff"/>
          <rect x="5.5" y="8.3" width="7" height="4.5" rx="1" fill="#fff"/>
          <circle cx="9" cy="10.5" r="1.2" fill="#c4173f"/>
        </svg>
        0438 715 642
      </li>
      <li class="contacts__item">
        <svg class="contacts__icon" viewBox="0 0 18 18" aria-hidden="true">
          <circle cx="9" cy="9" r="9" fill="#c4173f"/>
          <rect x="4.5" y="5.8" width="9" height="6.4" fill="none" stroke="#fff" stroke-width="1.2"/>
          <path d="M4.5 5.8 9 9.6l4.5-3.8" fill="none" stroke="#fff" stroke-width="1.2"/>
        </svg>
        boris@kvtlaw.co
      </li>
      <li class="contacts__item">
        <svg class="contacts__icon" viewBox="0 0 18 18" aria-hidden="true">
          <circle cx="9" cy="9" r="9" fill="#c4173f"/>
          <circle cx="9" cy="9" r="5" fill="none" stroke="#fff" stroke-width="1.2"/>
          <path d="M4 9h10M9 4c-2.2 2.8-2.2 7.2 0 10M9 4c2.2 2.8 2.2 7.2 0 10" fill="none" stroke="#fff" stroke-width="1"/>
        </svg>
        <span>www.<span class="contacts__hl">kvtlaw</span>.co</span>
      </li>
    </ul>

    <address class="address">
      Level 3, 118 Wexbury Street<br>
      Sydney NSW 2000
    </address>
  </section>

  <section class="card card--back">
    <div class="brand">
      <span class="brand__square"></span>
      <span class="brand__name">KVT LEGAL</span>
    </div>
  </section>
</body>
</html>
```